Bloom Ferry Kite Business cards

Logo, tag line and photo on card
Agent Name
Title
Address
Phone number
Email
Website
Make logo on one side large by rotating  to portrait format.  Keep the background of the logo white.

Contact Information for Business Card
Slogan; Keeping Each Kite Aloft

```html
<!DOCTYPE html>
<html lang="en">
<head>
<meta charset="utf-8">
<title>Bloom Ferry Kite — Business Cards</title>
<link rel="stylesheet" href="https://fonts.googleapis.com/css2?family=Saira:wght@400;700&family=Mrs+Saint+Delafield&display=swap">
<style>
  :root {
    --backdrop: #737373;
    --navy: #00266a;
    --navy-faint: #0a2f72;
    --red: #c8102e;
    --white: #ffffff;
    --grey-text: #7a7a7a;
    --rule: #444444;
    --photo-tone: #b9b9b9;
  }
  * { margin: 0; padding: 0; box-sizing: border-box; }
  html, body {
    width: 1200px; height: 1000px; overflow: hidden;
    background: var(--backdrop);
    font-family: "Saira", "Arial", sans-serif;
  }
  .card {
    position: absolute;
    left: 295px; width: 612px; height: 351px;
    border-radius: 28px;
    box-shadow: 0 18px 30px rgba(0,0,0,0.35);
  }
  .card-front { top: 126px; background: var(--navy); }
  .card-back { top: 538px; background: var(--white); }

  .front-mark {
    position: absolute; left: 0; right: 0; top: 88px;
    text-align: center;
    color: var(--navy-faint);
    font-weight: 700; font-size: 44px; line-height: 0.98;
    letter-spacing: -1px;
  }
  .tagline {
    position: absolute; left: 0; right: 0; top: 262px;
    text-align: center;
    color: var(--white);
    font-family: "Mrs Saint Delafield", cursive;
    font-size: 50px; line-height: 1;
  }

  .agent-photo {
    position: absolute; left: 57px; top: 48px;
    width: 111px; height: 111px; border-radius: 50%;
    border: 2px solid var(--red);
    padding: 4px;
    background: var(--white);
  }
  .agent-photo span {
    display: block; width: 100%; height: 100%; border-radius: 50%;
    background: radial-gradient(circle at 50% 45%, #cfcfcf, var(--photo-tone) 70%, #8f8f8f);
  }
  .agent-name {
    position: absolute; left: 57px; top: 186px;
    color: var(--navy); font-weight: 700; font-size: 20px; letter-spacing: 1.6px;
  }
  .agent-title {
    position: absolute; left: 57px; top: 209px;
    color: var(--red); font-size: 18px; letter-spacing: 1px;
  }
  .divider {
    position: absolute; left: 57px; top: 242px; width: 225px;
    border-top: 1px solid var(--rule);
  }
  .contact {
    position: absolute; left: 57px; top: 250px;
    list-style: none; color: var(--grey-text); font-size: 17px; line-height: 21px;
  }
  .brand-name {
    position: absolute; right: 50px; top: 54px;
    color: var(--navy); font-weight: 700; font-size: 30px; line-height: 0.95;
    text-align: center; letter-spacing: -0.5px;
  }
  .address {
    position: absolute; right: 51px; top: 304px;
    color: var(--grey-text); font-size: 14px; letter-spacing: 1px;
  }
</style>
</head>
<body>
  <section class="card card-front">
    <div class="front-mark">Bloom<br>Ferry<br>Kite</div>
    <p class="tagline">Keeping Each Kite Aloft</p>
  </section>

  <section class="card card-back">
    <div class="agent-photo" role="img" aria-label="Portrait photo of the agent"><span></span></div>
    <h1 class="agent-name">AGENT NAME</h1>
    <p class="agent-title">TITLE</p>
    <div class="divider"></div>
    <ul class="contact">
      <li>Phone number</li>
      <li>Email</li>
      <li>Website</li>
    </ul>
    <div class="brand-name">Bloom<br>Ferry<br>Kite</div>
    <p class="address">ADDRESS</p>
  </section>
</body>
</html>
```